Security Camera Sign

14” high x 11” wide Color: Blue, Yellow, Black and white

Make the sign vertical
Replace red with blue
WARNING: Black over yellow
These premises are protected by Closed Circuit Television: On white
Images are recorded for crime prevention and public safety. Unauthorized access, theft or vandalism will result in prosecution: On Blue

Target Market(s)

Outdoor commercial building

Industry/Entity Type

Security

Requirements
Nice to have
• I would like the sign stand out. If you need more colors? Thanks Ok

```html
<!DOCTYPE html>
<html lang="en">
<head>
<meta charset="utf-8">
<title>Security Camera Warning Sign</title>
<link rel="stylesheet" href="https://fonts.googleapis.com/css2?family=Archivo+Black&family=Arimo:wght@500;600&display=swap">
<style>
  :root {
    --backdrop: #6b6b6b;
    --sign-blue: #2e3192;
    --sign-white: #ffffff;
    --warning-yellow: #fff200;
    --ink-black: #000000;
    --camera-light: #e6e7e8;
    --camera-mid: #bcbec0;
    --camera-dark: #8a8c8e;
  }
  * { margin: 0; padding: 0; box-sizing: border-box; }
  html, body {
    width: 1200px;
    height: 1200px;
    overflow: hidden;
    background: var(--backdrop);
  }
  .canvas {
    position: relative;
    width: 1200px;
    height: 1200px;
  }
  /* 11in wide x 14in high */
  .sign {
    position: absolute;
    left: 176px;
    top: 60px;
    width: 848px;
    height: 1080px;
    border-radius: 34px;
    overflow: hidden;
    background: var(--sign-white);
    display: flex;
    flex-direction: column;
  }
  .header-band {
    flex: 0 0 170px;
    background: var(--sign-blue);
    display: flex;
    align-items: center;
    justify-content: center;
  }
  .warning-label {
    width: 700px;
    height: 110px;
    background: var(--warning-yellow);
    border: 2px solid var(--ink-black);
    border-radius: 9px;
    display: flex;
    align-items: center;
    justify-content: center;
    font-family: "Archivo Black", "Arial Black", sans-serif;
    font-size: 86px;
    letter-spacing: 2px;
    color: var(--ink-black);
    line-height: 1;
  }
  .notice-area {
    flex: 1 1 auto;
    display: flex;
    flex-direction: column;
    align-items: center;
    justify-content: center;
    gap: 40px;
    padding: 30px 0;
  }
  .notice-text {
    text-align: center;
    font-family: "Archivo Black", "Arial Black", sans-serif;
    font-size: 46px;
    line-height: 62px;
    color: var(--sign-blue);
  }
  .camera-illustration {
    width: 540px;
    height: 360px;
    border-radius: 24px;
    background: linear-gradient(150deg, var(--camera-light) 0%, var(--camera-mid) 60%, var(--camera-dark) 100%);
  }
  .footer-band {
    flex: 0 0 220px;
    background: var(--sign-blue);
    display: flex;
    align-items: center;
    justify-content: center;
    padding: 0 40px;
  }
  .legal-text {
    font-family: "Arimo", Arial, sans-serif;
    font-weight: 600;
    font-size: 28px;
    line-height: 40px;
    color: var(--sign-white);
    text-align: center;
  }
</style>
</head>
<body>
  <main class="canvas">
    <section class="sign">
      <header class="header-band">
        <div class="warning-label">WARNING</div>
      </header>

      <div class="notice-area">
        <p class="notice-text">THESE PREMISES<br>ARE PROTECTED BY<br>CLOSED CIRCUIT<br>TELEVISION</p>
        <div class="camera-illustration" role="img" aria-label="Illustration of a wall-mounted CCTV security camera"></div>
      </div>

      <footer class="footer-band">
        <p class="legal-text">IMAGES ARE RECORDED FOR CRIME PREVENTION<br>AND PUBLIC SAFETY. UNAUTHORIZED ACCESS,<br>THEFT OR VANDALISM WILL RESULT<br>IN PROSECUTION</p>
      </footer>
    </section>
  </main>
</body>
</html>
```